Web page for organic mosquito control company in Texas

Looking for a webpage that communicates the three main objectives of the company: Guaranteed effective, Affordable Rates, Organic Solution.
The company specializes in safe organic mosquito control. Service is conducted monthly during the mosquito season. What makes Quillmoor unique is the fact that it does not employ heavy pesticides, expensive equipment purchases and no nozzles misting installed throughout the property. I have some videos that I want to integrate. Please specify what format and codec do want the multi media file in?
Target Market(s)
Mothers 30-55 years of age
Industry/Entity Type
It Company
Number of Pages Required
5+ page
Requirements
Must have
- Predominant space for video on the home page
Nice to have
- Environmental theme without overdoing it.

```html
<!DOCTYPE html>
<html lang="en">
<head>
<meta charset="utf-8">
<title>Quillmoor Mosquito Control System</title>
<link rel="stylesheet" href="https://fonts.googleapis.com/css2?family=Open+Sans:wght@300;400;600;700&display=swap">
<style>
:root{
  --topbar:#3b3b3b;
  --orange:#e8860b;
  --orange-deep:#df7d00;
  --orange-btn:#d9770a;
  --leaf:#8dc63f;
  --leaf-pale:#d9f0b6;
  --label-green:rgba(86,168,104,.92);
  --charcoal:#2c2c2c;
  --rule:#4a4a4a;
  --ink:#2b2b2b;
  --white:#ffffff;
  --paper-line:#e4e4e4;
}
*{box-sizing:border-box;margin:0;padding:0}
html,body{width:1200px;height:2222px;overflow:hidden}
body{font-family:"Open Sans",Arial,sans-serif;background:var(--white);position:relative;color:var(--ink)}
.abs{position:absolute}

/* top bar */
.topbar{left:0;top:0;width:1200px;height:38px;background:var(--topbar);color:#e8e8e8;font-size:11px}
.topbar .item{position:absolute;top:11px;display:flex;align-items:center;gap:6px;white-space:nowrap}
.topbar svg{width:11px;height:11px;fill:#e8e8e8}
.social{position:absolute;top:6px;left:1000px;display:flex;gap:10px}
.social span{width:26px;height:26px;border:2px solid var(--orange);border-radius:50%;display:block}

/* header */
.header{left:0;top:38px;width:1200px;height:107px;background:linear-gradient(180deg,#f09417,#e8860b 70%,#e1800a);z-index:2}
.brand{position:absolute;left:44px;top:32px;display:flex;align-items:center;gap:10px}
.brand i{width:18px;height:18px;border-radius:50%;background:#3d6b1e;display:block}
.brand b{font-weight:700;font-size:30px;color:#3d6b1e;letter-spacing:-.5px}
.nav{position:absolute;right:57px;top:44px;display:flex;gap:17px;font-size:14px;color:var(--white);white-space:nowrap}

/* hero */
.hero{left:0;top:145px;width:1200px;height:360px;background:linear-gradient(120deg,#c9d8b5 0%,#e7d9c4 30%,#f1e3d2 50%,#a8c38a 75%,#d9dfd2 100%)}
.hero-label{left:10px;top:365px;width:462px;height:59px;background:var(--label-green);color:var(--white);font-weight:300;font-size:44px;line-height:59px;padding-left:18px}

/* intro */
.intro{left:0;top:504px;width:1200px;height:430px;background:var(--leaf)}
.intro h2{position:absolute;left:38px;width:535px;top:40px;text-align:center;color:var(--white);font-weight:400;font-size:35px}
.intro .copy{position:absolute;left:38px;top:86px;width:535px;font-size:13.2px;line-height:21.6px;color:#1d2a0e;text-align:justify}
.intro .copy p+p{margin-top:11px}
.btn{display:inline-block;background:var(--orange-btn);color:var(--white);font-size:12px;font-weight:600;border-radius:3px;box-shadow:0 2px 0 #a85a00}
.intro .btn{position:absolute;left:261px;top:360px;width:80px;height:30px;line-height:30px;text-align:center}
.video-title{position:absolute;left:613px;top:40px;font-weight:300;font-size:35px;color:var(--leaf-pale)}
.video{position:absolute;left:613px;top:88px;width:534px;height:296px;background:radial-gradient(ellipse at 55% 45%,#7a5a44 0%,#4a3d35 30%,#1a1a1a 70%)}
.video .vt{position:absolute;left:12px;top:8px;color:var(--white);font-size:12px}
.video .play{position:absolute;left:237px;top:124px;width:68px;height:48px;background:rgba(20,20,20,.85);border-radius:10px}

/* how it works */
.how{left:0;top:934px;width:1200px;height:437px;background:var(--charcoal);color:var(--white)}
.how h2{position:absolute;left:0;width:1200px;top:8px;text-align:center;font-weight:400;font-size:36px}
.how .lead{position:absolute;left:38px;top:64px;width:1110px;font-size:12.8px;line-height:20px;color:#8a8a8a}
.step{position:absolute;top:138px;width:286px;text-align:center}
.step .ico{width:57px;height:57px;margin:0 auto;background:var(--orange);border-radius:3px;display:flex;align-items:center;justify-content:center}
.step .ico svg{width:30px;height:30px}
.step h3{margin-top:26px;font-weight:400;font-size:22px;line-height:25px;color:#f1f1f1}
.step p{margin:22px auto 0;width:242px;font-size:12.5px;line-height:20.5px;color:#a5a5a5}
.step p.em{font-style:italic}
.step .more{margin-top:12px;font-size:11.5px;color:var(--orange)}
.divider{position:absolute;top:134px;width:1px;height:230px;background:var(--rule)}
.totop{left:1138px;top:1283px;width:32px;height:32px;border-radius:50%;background:#5a3a1a}

/* story */
.gap{left:0;top:1371px;width:1200px;height:19px;background:#f2f2f2}
.story{left:0;top:1390px;width:1200px;height:466px;background:var(--orange-deep)}
.story .story-title{position:absolute;left:38px;width:722px;top:38px;text-align:center;color:var(--white);font-weight:400;font-size:22px}
.story .copy{position:absolute;left:38px;top:84px;width:722px;font-size:12.8px;line-height:21.5px;color:#2a1a00}
.story .copy p+p{margin-top:11px}
.story .btn{height:24px;line-height:24px;padding:0 12px;font-size:11.5px;margin-left:4px}
.faq{position:absolute;top:311px;height:45px;border:2px solid var(--white);border-radius:4px;color:var(--white);font-size:17px;line-height:41px;text-align:center}
.story .reach{position:absolute;left:803px;width:344px;top:30px;text-align:center;font-weight:400;font-size:36px;color:var(--white)}
.field{position:absolute;left:803px;width:344px;background:var(--white);font-size:12.5px;color:#666;padding:0 12px;border-bottom:1px solid var(--paper-line)}
.story .send{position:absolute;left:803px;top:390px;width:103px;height:24px;line-height:24px;text-align:center;font-size:11.5px;padding:0;margin:0}

/* bottom */
.col-head{position:absolute;top:1874px;font-size:17px;font-weight:400;color:#333;text-transform:uppercase}
.testimonial{left:38px;top:1904px;width:343px;height:243px;border:1px solid #ddd;border-radius:4px;padding:26px 18px;font-size:13.5px;line-height:21px;color:#222}
.avatar{position:absolute;left:22px;top:180px;width:46px;height:46px;border-radius:50%;background:linear-gradient(#5da845,#2f7a32)}
.who{position:absolute;left:80px;top:193px;font-size:13.5px;color:#aaa}
.dots{left:198px;top:2162px;display:flex;gap:6px}
.dots span{width:4px;height:4px;border-radius:50%;background:#aaa}
.dots span:first-child{background:var(--orange)}
.blog{left:421px;top:1904px;width:340px}
.blog h4{font-weight:400;font-size:21px;color:#ccc}
.blog .meta{margin-top:10px;font-size:11px;color:#bbb}
.blog .meta span{margin:0 6px}
.blog p{margin-top:12px;font-size:13.5px;line-height:21px;color:#888}
.blog .date{margin-top:10px;text-align:right;font-size:12px;color:var(--orange)}
.photo{position:absolute;top:1904px;height:202px}
.arrow{position:absolute;top:1976px;width:24px;height:58px;background:var(--orange);display:flex;align-items:center;justify-content:center}
.footer-rule{left:0;top:2186px;width:1200px;height:1px;background:#ddd}
</style>
</head>
<body>

<div class="abs topbar">
  <div class="item" style="left:40px"><svg viewBox="0 0 10 10"><path d="M5 0a3.5 3.5 0 0 0-3.5 3.5C1.5 6 5 10 5 10s3.5-4 3.5-6.5A3.5 3.5 0 0 0 5 0zm0 5a1.5 1.5 0 1 1 0-3 1.5 1.5 0 0 1 0 3z"/></svg>412 Alder Street, Suite 108 Kingsford, Ontario K7P 3R4 Canada</div>
  <div class="item" style="left:410px"><svg viewBox="0 0 10 10"><path d="M2 0l2 2.5-1 1.5c.6 1.3 1.6 2.3 3 3l1.5-1L10 8 8.5 10C4 9.5.5 6 0 1.5z"/></svg>+1 555 0142 8830</div>
  <div class="item" style="left:535px"><svg viewBox="0 0 10 10"><path d="M0 2h10v6H0zm1 1l4 3 4-3"/></svg>info@quillmoor.com</div>
  <div class="item" style="left:672px"><svg viewBox="0 0 10 10"><circle cx="5" cy="5" r="4.5" fill="none" stroke="#e8e8e8"/><path d="M5 2v3h2" stroke="#e8e8e8" fill="none"/></svg>9am to 4pm</div>
  <div class="item" style="left:788px">Customer Support</div>
  <div class="item" style="left:901px">Download</div>
  <div class="social"><span></span><span></span><span></span><span></span><span></span></div>
</div>

<header class="abs header">
  <div class="brand"><i></i><b>Quillmoor</b></div>
  <nav class="nav">
    <span>HOME</span>
    <span>ABOUT US ▾</span>
    <span>QUILLMOOR SOLUTION ▾</span>
    <span>PRICE ▾</span>
    <span>HOW IT WORKS ? ▾</span>
    <span>F A Q ▾</span>
    <span>CONTACT</span>
  </nav>
</header>

<div class="abs hero" role="img" aria-label="Photo of a smiling family with two young children planting in a sunny garden"></div>
<div class="abs hero-label">Guaranteed effective</div>

<section class="abs intro">
  <h2>Mosquito Freedom!</h2>
  <div class="copy">
    <p>Designed in Texas by Texans, specifically for Texas Mosquitoes, the Quillmoor Mosquito Control System is the first organically-based mosquito control system that eliminates both mosquitoes and the need for automatic mosquito misting systems.Our 99.5% organic solution not only minimizes your family's risk to harmful pathogens such as West Nile Virus, Chikungunya, and Eastern Equine Encephalitis, but it also reduces pesticide exposure by 95% compared to nozzle misting systems.&nbsp; Better yet, our customer's report the Quillmoor system is nearly twice as effective as expensive nozzle systems.Throw away the sprays, magnets, fans, and other gimmicks that offer little in effectiveness.</p>
    <p>The Quillmoor Mosquito Control System is the only effective and guaranteed method of ridding those annoying mosquitoes, protecting your health, and enjoying your outdoor living environment to the fullest.</p>
  </div>
  <span class="btn">read more</span>
  <div class="video-title">Watch the video</div>
  <div class="video" role="img" aria-label="Video still: close-up of a mosquito head">
    <span class="vt">Mosquito Week</span>
    <svg class="abs" style="right:8px;top:8px" width="12" height="12" viewBox="0 0 12 12"><circle cx="9.5" cy="2.5" r="2" fill="#fff"/><circle cx="2.5" cy="6" r="2" fill="#fff"/><circle cx="9.5" cy="9.5" r="2" fill="#fff"/><path d="M9.5 2.5L2.5 6l7 3.5" stroke="#fff" fill="none"/></svg>
    <div class="play"><svg width="68" height="48" viewBox="0 0 68 48"><path d="M28 16l14 8-14 8z" fill="#fff"/></svg></div>
  </div>
</section>

<section class="abs how">
  <h2>How the Quillmoor Mosquito Control System works</h2>
  <p class="lead">Mosquitoes have four distinct life stages (egg, larvae, pupae, adult). Most mosquito control methods fail to control mosquito populations by focusing inadequately ononlyone of these life stages. The Quillmoor Mosquito Control System focuseson the eradication of allfourlife stages to achieve 90%+ eradication of the mosquito population on a property</p>

  <div class="step" style="left:19px">
    <div class="ico"><svg viewBox="0 0 30 30"><circle cx="13" cy="13" r="8" fill="none" stroke="#fff" stroke-width="4"/><path d="M19 19l7 7" stroke="#fff" stroke-width="5" stroke-linecap="round"/></svg></div>
    <h3>Remedying Conducive<br>Conditions</h3>
    <p>Before a service can commence, a licensed technician will inspect and identify areas to be addressed that are contributing to mosquito harborages..</p>
    <div class="more">read more ›</div>
  </div>
  <div class="divider" style="left:306px"></div>
  <div class="step" style="left:306px">
    <div class="ico"><svg viewBox="0 0 30 30"><circle cx="15" cy="15" r="10" fill="none" stroke="#fff" stroke-width="4"/><path d="M8 22L22 8" stroke="#fff" stroke-width="4"/></svg></div>
    <h3>Eradication of adult<br>mosquitoes</h3>
    <p class="em">Utilizing the most powerful equipment available, technicians direct a pyrethrum-based adulticide deep into mosquito harborages at a velocity of</p>
    <div class="more"><i style="color:#a5a5a5;font-size:12.5px">140 mph</i> read more ›</div>
  </div>
  <div class="divider" style="left:594px"></div>
  <div class="step" style="left:594px">
    <div class="ico"><svg viewBox="0 0 30 30"><path d="M11 4h8M12 4v9L5 25h20L18 13V4" fill="#fff" stroke="#fff" stroke-width="2" stroke-linejoin="round"/></svg></div>
    <h3>Repelling adult<br>mosquitoes</h3>
    <p>A mixture of unique essential oils in the Quillmoor solution serve as a strong repellant, preventing mosquitoes from nesting on the property.</p>
    <div class="more">read more ›</div>
  </div>
  <div class="divider" style="left:880px"></div>
  <div class="step" style="left:880px">
    <div class="ico"><svg viewBox="0 0 30 30"><path d="M5 15l7 7L25 8" fill="none" stroke="#fff" stroke-width="5"/></svg></div>
    <h3>Sterilizing mosquito<br>larvae</h3>
    <p>When standing water cannot be remedied, the Quillmoor Mosquito Control System utilizes insect-growth-regulators, to treat water receptacles</p>
    <div class="more">read more ›</div>
  </div>
</section>
<div class="abs totop"><svg width="32" height="32" viewBox="0 0 32 32"><path d="M11 18l5-5 5 5" stroke="#fff" stroke-width="2.5" fill="none"/></svg></div>

<div class="abs gap"></div>
<section class="abs story">
  <h2 class="story-title">The Birth of the Quillmoor Mosquito Control System</h2>
  <div class="copy">
    <p>The company's founders, Dalton Crewe and Marcus Heller have been in the pest control business since 1996. Understanding the life cycles, environments, and habits of all household pests have resulted in effective treatments designed to eliminate pests while minimizing pesticide exposure to their customers.&nbsp; Continually seeking for ways to improve their service led them to their discovery of the Quillmoor Mosquito Control System.</p>
    <p>What initially motivated the founders is that they are parents of small children and found themselves frustrated with the hazards and annoyance of mosquitoes at their own homes, and the inadequate solutions available to the public.</p>
    <p>This propelled the founders into a quest to find a productto tackle the problem of mosquitoes that was</p>
    <p>1) Effective 2) Affordable 3) Natural and 4) Safe. <span class="btn">read more ..</span></p>
  </div>
  <div class="faq" style="left:38px;width:162px">SERVICE F A Q</div>
  <div class="faq" style="left:293px;width:181px">MOSQUITO F A Q</div>
  <div class="faq" style="left:547px;width:162px">DISEASE F A Q</div>

  <h2 class="reach">Reach to us</h2>
  <div class="field" style="top:92px;height:38px;line-height:38px;border-radius:3px 3px 0 0">Name *</div>
  <div class="field" style="top:130px;height:39px;line-height:39px">E-mail *</div>
  <div class="field" style="top:169px;height:38px;line-height:38px;border-radius:0 0 3px 3px">Telephone</div>
  <div class="field" style="top:226px;height:144px;padding-top:10px;border-radius:3px">Message *</div>
  <span class="btn send">Send message</span>
</section>

<h3 class="col-head" style="left:38px">Client Testimonial</h3>
<h3 class="col-head" style="left:421px">Blogs &amp; News</h3>
<h3 class="col-head" style="left:803px">Photo Gallery</h3>

<div class="abs testimonial">
  Lorem Ipsum is simply dummy text of the printing and typesetting industry. Lorem Ipsum has been the industry's standard dummy text ever since the 1500s, when an unknown printer took a galley of type and scrambled it to make a type specimen book. It has survived not only five centuries,
  <div class="avatar" role="img" aria-label="Client portrait"></div>
  <div class="who">Anjali Mehra – UAE</div>
</div>
<div class="abs dots"><span></span><span></span><span></span></div>

<div class="abs blog">
  <h4>Hello world!</h4>
  <div class="meta">By admin <span>|</span> Uncategorized <span>|</span> 1 Comment</div>
  <p>Welcome to Inkpress. This is your first post. Edit or delete it, then start blogging!</p>
  <div class="date">February 7, 2015 ✎</div>
</div>

<div class="photo" style="left:803px;width:271px;background:linear-gradient(180deg,#c9d3dc 0%,#aab4bf 40%,#e6ebef 65%,#d3d8dd 100%)" role="img" aria-label="Photo of people skating on an outdoor ice rink in winter"></div>
<div class="photo" style="left:1093px;width:54px;background:linear-gradient(180deg,#8a7a62,#cfc7b8)" role="img" aria-label="Gallery photo"></div>
<div class="arrow" style="left:810px;opacity:.6"><svg width="10" height="16" viewBox="0 0 10 16"><path d="M8 2L2 8l6 6" stroke="#fff" stroke-width="2" fill="none"/></svg></div>
<div class="arrow" style="left:1115px"><svg width="10" height="16" viewBox="0 0 10 16"><path d="M2 2l6 6-6 6" stroke="#fff" stroke-width="2" fill="none"/></svg></div>

<div class="abs footer-rule"></div>
</body>
</html>
```